Direct Mail Letter / Reply Device / Outer Envelope

I'm interested in seeing if I can give my charity's annual appeal a fresh look and feel. I have written the letter though edits might be needed. We're really looking for 'pop'. Edits to the letter will need to happen before our final design. My budget for design is about $250.00 but I may be able to negotiate for the right design.

Target Market(s)

Donors to a specific charity

Font styles to use
Serif
Sans Serif

Colors

Designer to choose colors to be used in the design.

Requirements
Must have
• Color photos that make the most of the photos I have regardless of resolutions. I need something in a format that will let me make edits and / or reuse next year or for my thank you letter. Basically, a Word friendly version.

```html
<!DOCTYPE html>
<html lang="en">
<head>
<meta charset="utf-8">
<title>Lab Haven – Annual Appeal Letter</title>
<link href="https://fonts.googleapis.com/css2?family=Raleway:wght@300;400;800&display=swap" rel="stylesheet">
<style>
  :root {
    --teal-deep: #1e4d5c;
    --teal-mid: #1f8ea3;
    --teal-bright: #0a9bb5;
    --teal-soft: #2a9ab0;
    --teal-light: #5fb6c6;
    --mist: #e6efee;
    --ink: #1d1d1d;
    --muted: #8a8f93;
    --rule: #6d8a94;
    --web: #555a5e;
    --paper: #ffffff;
  }
  * { margin: 0; padding: 0; box-sizing: border-box; }
  html, body { width: 849px; height: 1200px; overflow: hidden; background: var(--paper); }
  .letterhead {
    position: relative;
    width: 849px;
    height: 1200px;
    overflow: hidden;
    font-family: "Raleway", sans-serif;
    color: var(--ink);
  }
  .header-art { position: absolute; top: 0; left: 0; }
  .background-shape { position: absolute; left: 0; top: 560px; }
  .brand-mark {
    position: absolute;
    left: 101px;
    top: 66px;
    width: 244px;
    height: 244px;
    display: flex;
    flex-direction: column;
    align-items: center;
    justify-content: center;
    gap: 14px;
    color: var(--paper);
  }
  .brand-dot { width: 12px; height: 12px; background: var(--paper); border-radius: 50%; }
  .brand-name {
    font-family: "Raleway", sans-serif;
    font-weight: 400;
    font-size: 34px;
    line-height: 1;
  }
  .letter-body {
    position: absolute;
    left: 154px;
    top: 380px;
    width: 560px;
    font-size: 15.3px;
    font-weight: 300;
    line-height: 24.9px;
  }
  .letter-body p { margin-bottom: 9px; }
  .letter-body strong { font-weight: 800; }
  .footer {
    position: absolute;
    left: 154px;
    top: 1082px;
    width: 542px;
    border-top: 1px solid var(--rule);
    text-align: center;
    color: var(--muted);
  }
  .footer-contact { font-size: 13.6px; font-weight: 300; margin-top: 12px; }
  .footer-web { font-size: 13.6px; font-weight: 800; color: var(--web); margin-top: 7px; }
</style>
</head>
<body>
<div class="letterhead">
  <svg class="background-shape" width="849" height="640" viewBox="0 0 849 640" role="img" aria-label="Large faint decorative shape behind the letter text">
    <path d="M0 225 C200 180 420 140 560 170 C680 195 720 260 690 330 C660 400 640 480 700 640 L0 640 Z" fill="var(--mist)"/>
  </svg>

  <svg class="header-art" width="849" height="320" viewBox="0 0 849 320" aria-hidden="true">
    <defs>
      <linearGradient id="bandGrad" x1="0" y1="0" x2="1" y2="0.4">
        <stop offset="0" stop-color="var(--teal-bright)"/>
        <stop offset="0.5" stop-color="var(--teal-mid)"/>
        <stop offset="1" stop-color="var(--teal-soft)"/>
      </linearGradient>
    </defs>
    <polygon points="0,0 849,0 849,300 352,176 104,144 0,172" fill="url(#bandGrad)"/>
    <polygon points="0,88 110,150 0,172" fill="var(--teal-light)" opacity="0.55"/>
    <polygon points="530,0 849,0 849,200" fill="var(--teal-soft)" opacity="0.6"/>
    <polygon points="330,0 530,0 400,110" fill="var(--teal-bright)" opacity="0.5"/>
    <circle cx="223" cy="188" r="128" fill="var(--paper)"/>
    <circle cx="223" cy="188" r="122" fill="var(--teal-deep)"/>
  </svg>

  <div class="brand-mark">
    <span class="brand-dot"></span>
    <span class="brand-name">Lab Haven</span>
  </div>

  <main class="letter-body">
    <p>Dear [First Name]</p>
    <p>It’s another extraordinary year for Lab Haven HVLR. This year, I write to<br>you for the first time, as the President of Lab Haven. After more than a<br>decade of involvement with the Haven, it’s remarkable to reflect on how<br>the Haven has grown and adapted to meet the needs of homeless Labs.</p>
    <p>After starting as a small volunteer organization rescuing just one or two<br>hundred Labs a year, we have grown to an organization with hundreds<br>of volunteers working to save nearly 1,000 Labs each year. This year has<br>involved its own set of new challenges and new achievements.</p>
    <p>For the past several years, we’ve witnessed an increase in eager adopters<br>- more caring people willing and able to provide a loving home for a Lab<br>(or two) for the rest of their lives. We are delighted to find Labs in need<br>for these wonderful people. For the past two years we have reached<br>beyond our previous geographic region to areas where the numbers of<br>dogs in need is heartbreaking. We are so glad to offer hope where there<br>previously was none.</p>
    <p>At the same time, we’ve seen the Labs that make their way to the local<br>shelters we have worked with for many years change. <strong>We are now<br>routinely approached to save an increasing number of older Labs and<br>Labs with pre-existing conditions that others can’t afford to fix.</strong></p>
    <p>Lab Haven of the HVLR has always been a group that saves everyone<br>who can be saved.  What that often means is we must spend more<br>money and keep a needy Lab in our care for much longer. Last year,<br>we rescued and restored sight to Helen, a blind, diabetic 9 year old<br>who had suffered from years of neglect. Helen remained in Lab Haven</p>
  </main>

  <footer class="footer">
    <p class="footer-contact">Lab Line: (555) 014-2290 &nbsp;| P.O. Box 4217 Millbrook VA 22190</p>
    <p class="footer-web">www.lab-haven.org</p>
  </footer>
</div>
</body>
</html>
```